Thrifty Haul: Junk Removal - Website Design

We need a design and uploaded to Hostivra.com. I enclosed our postcard for reference too. I need a contact from at the top right so I can get leads.

Here are the sites I like:

https://trykemvan.com/
https://www.1800zibwaste.com
https://www.brindlemoversclearingco.com/junk-removal/
http://anookforgrams.com/
http://www.drivelunt.com/alternate/
https://www.servicevangifting.org/
http://www.autosforpatriots.org/indexj/

Coding

Coded - Design and coding required

Number of Pages Required

1 page

```html
<!DOCTYPE html>
<html lang="en">
<head>
<meta charset="utf-8">
<title>Thrifty Haul – Junk Removal</title>
<link rel="stylesheet" href="https://fonts.googleapis.com/css2?family=Oswald:wght@300;400;600;700&family=Open+Sans:ital,wght@0,300;0,400;0,600;0,700;1,300&display=swap">
<style>
:root{
  --green:#76b82a;
  --navy:#0d3281;
  --text:#333;
  --muted:#555;
  --light:#f2f3f7;
  --grey:#f0f0f0;
  --white:#fff;
}
*{box-sizing:border-box;margin:0;padding:0}
html,body{width:1200px;height:2794px;overflow:hidden}
body{position:relative;font-family:"Open Sans",sans-serif;color:var(--text);background:var(--white)}
.abs{position:absolute}
.heading{font-family:"Oswald",sans-serif;font-weight:700;color:var(--navy);text-transform:uppercase}
.btn{position:absolute;background:var(--green);color:var(--white);font-weight:600;font-size:15px;display:flex;align-items:center;justify-content:center;text-transform:uppercase;border-radius:2px}

/* header */
.header{top:0;left:0;width:1200px;height:113px;background:var(--white)}
.brand{left:137px;top:20px;width:278px;height:68px;background:#f7f7f7;display:flex;align-items:center;justify-content:center;font-family:"Oswald",sans-serif;font-weight:700;font-size:48px;color:var(--green);text-transform:uppercase;letter-spacing:-.5px}
.hotline{right:143px;top:14px;font-family:"Oswald",sans-serif;font-weight:300;font-size:19px;color:var(--green);display:flex;align-items:center;gap:8px}
.hotline b{font-weight:600}
.nav{right:143px;top:54px;display:flex;gap:31px;font-family:"Oswald",sans-serif;font-size:14px;color:#222;text-transform:uppercase;align-items:center}
.nav .active{color:var(--navy);border-bottom:2px solid var(--navy);padding-bottom:6px;margin-top:8px}

/* hero */
.hero{top:113px;left:0;width:1200px;height:563px;background:linear-gradient(100deg,#3a5b8c 0%,#6a7f9c 35%,#b79a74 60%,#a98966 100%)}
.hero-title{left:142px;top:282px;font-family:"Oswald",sans-serif;font-weight:700;font-size:64px;color:var(--white);text-transform:uppercase;line-height:1}
.hero-sub{left:143px;top:363px;font-size:21px;color:#f0f0f0;text-transform:uppercase}
.dots{display:flex;gap:7px}
.dots i{display:block;width:9px;height:9px;border-radius:50%;background:var(--white)}
.dots i.off{background:transparent;border:1px solid var(--white)}

/* quote form */
.form-head{left:736px;top:90px;width:299px;height:83px;background:var(--green);color:var(--white);font-family:"Oswald",sans-serif;font-size:21px;text-align:center;line-height:29px;padding-top:12px}
.form-body{left:736px;top:173px;width:299px;height:350px;background:var(--navy)}
.field{position:absolute;background:var(--white);height:41px;font-size:14px;color:#444;padding:0 14px;display:flex;align-items:center}

/* welcome */
.welcome-title{left:145px;top:740px;font-size:36px;line-height:42px}
.welcome-text{left:145px;width:440px;font-size:14px;line-height:23px;color:var(--text)}
.photo-frame{left:641px;top:748px;width:416px;height:325px;background:var(--white);box-shadow:0 1px 8px rgba(0,0,0,.25)}
.photo-frame div{position:absolute;left:8px;top:7px;width:400px;height:309px;background:linear-gradient(160deg,#5f8a3b 0%,#7a6a4c 55%,#8a3a2a 100%)}

/* services */
.services{top:1152px;left:0;width:1200px;height:482px;background:var(--light)}
.services-title{left:0;width:1200px;top:1212px;text-align:center;font-size:35px}
.service{position:absolute;top:1289px;width:270px;text-align:center}
.service .icon{width:126px;height:126px;border-radius:50%;background:var(--white);margin:0 auto;display:flex;align-items:center;justify-content:center}
.service h3{font-family:"Oswald",sans-serif;font-weight:400;font-size:20px;color:var(--navy);margin-top:10px}
.service p{font-size:14px;line-height:26px;color:var(--muted);margin-top:4px}

/* why */
.why{top:1634px;left:0;width:1200px;height:374px;background:linear-gradient(180deg,#4d3b3e 0%,#6a3a44 50%,#4a3b3a 100%)}
.why-title{left:0;width:1237px;top:1698px;text-align:center;font-size:35px;color:var(--white)}
.why-text{left:0;width:1200px;top:1756px;text-align:center;font-size:17px;line-height:32px;color:#eee}
.perks{left:147px;top:1852px;width:905px;display:flex;justify-content:space-between;font-size:20px;font-weight:300;color:#f0f0f0}
.perks span{display:flex;align-items:center;gap:6px}

/* testimonial */
.testi{top:2008px;left:0;width:1200px;height:458px;background:var(--grey)}
.testi-title{left:0;width:1200px;top:2048px;text-align:center;font-size:35px}
.avatar{left:535px;top:2110px;width:130px;height:130px;border-radius:50%;border:3px solid var(--white);box-shadow:0 0 0 1px #ccc;background:linear-gradient(180deg,#a7b3c2,#c9d94a 60%,#2c4d8a)}
.quote{left:220px;width:760px;top:2252px;text-align:center;font-style:italic;font-weight:300;font-size:14px;line-height:22px;color:#444}
.qmark{font-family:Georgia,serif;font-size:48px;color:#ccc;line-height:1}
.client{left:0;width:1200px;top:2312px;text-align:center;font-weight:600;font-size:14px;color:var(--green)}
.client-role{left:0;width:1200px;top:2340px;text-align:center;font-size:11px;color:var(--navy)}
.tdots{left:572px;top:2396px;display:flex;gap:11px}
.tdots i{width:6px;height:6px;border-radius:50%;background:#bbb;display:block}
.tdots i.on{background:var(--navy)}

/* footer */
.footer{top:2466px;left:0;width:1200px;height:328px;background:var(--navy);color:var(--white)}
.fcol{position:absolute;top:2494px}
.fcol h4{font-weight:400;font-size:20px;margin-bottom:18px}
.fcol li{list-style:none;font-size:11.5px;line-height:29px}
.contact-row{display:flex;gap:8px;font-size:11.5px;line-height:18px;margin-bottom:16px}
.contact-row.big{font-size:15px;font-weight:600}
.socials{display:flex;gap:6px}
.socials i{display:block;width:34px;height:34px;border-radius:50%;background:var(--white)}
.copy{left:0;width:1200px;top:2750px;text-align:center;font-size:11.5px;color:#e6e6e6}
</style>
</head>
<body>

<header class="abs header">
  <div class="abs brand">Thrifty Haul</div>
  <div class="abs hotline">
    <svg width="26" height="26" viewBox="0 0 24 24" fill="none" stroke="#76b82a" stroke-width="1.3"><path d="M5 3l3 0 1.5 4-2 1.5a11 11 0 0 0 8 8l1.5-2 4 1.5v3a2 2 0 0 1-2 2A17 17 0 0 1 3 5a2 2 0 0 1 2-2z"/></svg>
    <span>24/7 Customer Service <b>1-800-555-0148</b></span>
  </div>
  <nav class="abs nav">
    <span class="active">Home</span><span>About Us</span><span>Junk Removal</span><span>Our Services</span><span>Features</span>
    <span style="display:flex;align-items:center;gap:10px">Contact Us
      <svg width="28" height="15"><rect width="28" height="15" fill="#1f3b8c"/><rect x="12" width="4" height="15" fill="#fff"/><rect y="5.5" width="28" height="4" fill="#fff"/><rect x="13" width="2" height="15" fill="#d2232a"/><rect y="6.5" width="28" height="2" fill="#d2232a"/></svg>
      <svg width="8" height="5"><path d="M0 0h8L4 5z" fill="#333"/></svg>
    </span>
  </nav>
</header>

<section class="abs hero" role="img" aria-label="Mover in blue overalls carrying cardboard boxes"></section>
<div class="abs hero-title">Thrifty Haul</div>
<div class="abs hero-sub">America's most trusted name in junk removal</div>
<div class="btn" style="left:144px;top:421px;width:143px;height:45px">Contact Us</div>
<div class="abs dots" style="left:579px;top:637px"><i class="off"></i><i></i><i></i></div>

<svg class="abs" style="left:709px;top:90px" width="27" height="24"><path d="M27 0V24H0z" fill="#5e9620"/></svg>
<svg class="abs" style="left:1035px;top:90px" width="22" height="24"><path d="M0 0V24H22z" fill="#5e9620"/></svg>
<div class="abs form-head">Get Free Quotes from Junk<br>Removal Services</div>
<form class="abs form-body">
  <div class="field" style="left:17px;top:26px;width:127px">First Name *</div>
  <div class="field" style="left:157px;top:26px;width:127px">Last Name *</div>
  <div class="field" style="left:17px;top:82px;width:267px">Phone Number *</div>
  <div class="field" style="left:17px;top:137px;width:267px">Email Address *</div>
  <div class="field" style="left:17px;top:193px;width:267px;justify-content:space-between">State <svg width="9" height="5"><path d="M0 0h9L4.5 5z" fill="#222"/></svg></div>
  <div class="btn" style="left:17px;top:261px;width:167px;height:50px;font-size:15px">Get Quote Now</div>
</form>

<h1 class="abs heading welcome-title">Welcome to<br>Thrifty Haul</h1>
<p class="abs welcome-text" style="top:838px">Sed do eiusmod tempor incididunt ut labore et dolore magna aliqua. Ut enim ad minim veniam, quis nostrud exercitation ullamco laboris nisi ut aliquip ex ea commodo consequat.</p>
<p class="abs welcome-text" style="top:926px">Excepteur sint occaecat cupidatat non proident, sunt in culpa qui officia deserunt mollit anim id est laborum</p>
<div class="btn" style="left:145px;top:1016px;width:153px;height:52px;font-size:16px">Book Today</div>
<div class="abs photo-frame"><div role="img" aria-label="Worker loading old furniture onto a pickup truck"></div></div>

<section class="abs services"></section>
<h2 class="abs heading services-title">Our Services</h2>
<div class="service" style="left:133px">
  <div class="icon"><svg width="72" height="54" viewBox="0 0 72 54" fill="none" stroke="#76b82a" stroke-width="2.5"><rect x="4" y="4" width="64" height="8"/><path d="M4 12h64l-4 10H8z"/><path d="M10 22v30h52V22"/><rect x="16" y="28" width="22" height="14"/><rect x="44" y="28" width="12" height="24"/></svg></div>
  <h3>House/Garage/Estate Clean Out</h3>
  <p>Lorem ipsum dolor sit amet, consectetur adipiscing elit, sed do eiusmod tempor incididunt ut labore et dolore magna aliqua laboris nisi ut commodo.</p>
</div>
<div class="service" style="left:465px">
  <div class="icon"><svg width="72" height="70" viewBox="0 0 72 70" fill="none" stroke="#76b82a" stroke-width="3"><path d="M14 34V18a22 14 0 0 1 44 0v16"/><path d="M6 30h10v18H56V30h10v22H6z"/><path d="M22 40h28"/><path d="M10 52v8M62 52v8"/></svg></div>
  <h3>Furniture/Appliance Removal</h3>
  <p>Lorem ipsum dolor sit amet, consectetur adipiscing elit, sed do eiusmod tempor incididunt ut labore et dolore magna aliqua laboris nisi ut commodo.</p>
</div>
<div class="service" style="left:795px">
  <div class="icon"><svg width="50" height="60" viewBox="0 0 50 60" fill="none" stroke="#76b82a" stroke-width="2.5"><path d="M4 10h42M18 10V4h14v6"/><path d="M8 14l3 44h28l3-44z"/><path d="M18 20v32M25 20v32M32 20v32"/></svg></div>
  <h3>We Recycle</h3>
  <p>Lorem ipsum dolor sit amet, consectetur adipiscing elit, sed do eiusmod tempor incididunt ut labore et dolore magna aliqua laboris nisi ut commodo.</p>
</div>

<section class="abs why" role="img" aria-label="Full red dumpster of debris"></section>
<h2 class="abs heading why-title">Why choose Thrifty Haul?</h2>
<p class="abs why-text">Thrifty Haul is a full-service junk removal company serving areas across the United States.<br>We're in your neighborhood.</p>
<div class="abs perks">
  <span><svg width="17" height="17" viewBox="0 0 16 16"><circle cx="8" cy="8" r="8" fill="#fff"/><path d="M4.5 8.2l2.3 2.3 4.7-4.7" stroke="#6a3a44" stroke-width="2" fill="none"/></svg>On-time service</span>
  <span><svg width="17" height="17" viewBox="0 0 16 16"><circle cx="8" cy="8" r="8" fill="#fff"/><path d="M4.5 8.2l2.3 2.3 4.7-4.7" stroke="#6a3a44" stroke-width="2" fill="none"/></svg>Up front pricing</span>
  <span><svg width="17" height="17" viewBox="0 0 16 16"><circle cx="8" cy="8" r="8" fill="#fff"/><path d="M4.5 8.2l2.3 2.3 4.7-4.7" stroke="#6a3a44" stroke-width="2" fill="none"/></svg>Full-service junk removel</span>
  <span><svg width="17" height="17" viewBox="0 0 16 16"><circle cx="8" cy="8" r="8" fill="#fff"/><path d="M4.5 8.2l2.3 2.3 4.7-4.7" stroke="#6a3a44" stroke-width="2" fill="none"/></svg>Covid-19 compliant</span>
</div>

<section class="abs testi"></section>
<h2 class="abs heading testi-title">What our client saying</h2>
<div class="abs avatar" role="img" aria-label="Portrait of a client in a high-visibility jacket"></div>
<span class="abs qmark" style="left:192px;top:2234px">&ldquo;</span>
<p class="abs quote">At vero eos et accusamus et iusto odio dignissimos ducimus qui blanditiis praesentium voluptatum deleniti atque corrupti quos dolores et quas molestias excepturi sint occaecati cupiditate non provident</p>
<span class="abs qmark" style="left:872px;top:2274px">&rdquo;</span>
<div class="abs client">VOLUPTATE VELIT ESSE</div>
<div class="abs client-role">(ACCUSANTIUM DOLOREMQUE LAUDANTIUM, TOTAM)</div>
<div class="abs tdots"><i class="on"></i><i></i><i></i><i></i></div>

<footer class="abs footer"></footer>
<div class="fcol" style="left:144px;color:#fff"><h4>Company</h4><ul><li>Home</li><li>About Us</li><li>Who We Are</li><li>Pricing/Free</li><li>Trial</li></ul></div>
<div class="fcol" style="left:367px;color:#fff"><h4>Information</h4><ul><li>Privacy Policy</li><li>Terms &amp; Conditions</li><li>Who We Are</li><li>Blog</li><li>Contact</li></ul></div>
<div class="fcol" style="left:616px;color:#fff"><h4>Contact Us</h4>
  <div class="contact-row"><svg width="12" height="16" viewBox="0 0 12 16"><path d="M6 0a6 6 0 0 1 6 6c0 4-6 10-6 10S0 10 0 6a6 6 0 0 1 6-6z" fill="#fff"/><circle cx="6" cy="6" r="2.2" fill="#0d3281"/></svg><span>HaulPoint, Street Name,<br>City Name, Counrty Code.</span></div>
  <div class="contact-row big"><svg width="14" height="14" viewBox="0 0 24 24"><path d="M5 2h4l2 5-3 2a12 12 0 0 0 7 7l2-3 5 2v4a2 2 0 0 1-2 2A19 19 0 0 1 3 4a2 2 0 0 1 2-2z" fill="#fff"/></svg><span>1-800-555-0148</span></div>
  <div class="contact-row big"><svg width="15" height="14" viewBox="0 0 16 12"><rect width="16" height="12" rx="1" fill="#fff"/><path d="M0 1l8 6 8-6" stroke="#0d3281" stroke-width="1.5" fill="none"/></svg><span>info@thriftyhaul-mail.com</span></div>
</div>
<div class="fcol" style="left:902px;color:#fff"><h4>Connect With Us</h4><div class="socials"><i></i><i></i><i></i><i></i></div></div>
<div class="abs copy">Copyrights © 2020 Thrifty Haul. All rights reserved.</div>

</body>
</html>
```